Business card for Bio pharmaceutical company

Hello,
We are a bio pharmaceutical contract manufacturing company in Brisbane, Australia. Can you please create a new business card design. Please go to our website for colours http://www.velocrine.com.au.
On the back can you include the cartoon mascot Tobin Wuzzle and the tagline
"A Global Biopharmaceutical Contract Development Manufacturing Company"
Target Market(s)
Biotechnology
Industry/Entity Type
Pharmaceutical
Contact Information for Business Card
Maria Hollingby
Business Development Manager
maria.hollingby@velocrine.com.au
1947 Kelmott Street Parvale Queesnland 4213 Australia
T: +61 7 3590 2481
M +61 427 516 093
F +61 7 3648 2057
www.velocrine.com.au
Look and feel

```html
<!DOCTYPE html>
<html lang="en">
<head>
<meta charset="utf-8">
<title>Velocrine – Business Card</title>
<link rel="stylesheet" href="https://fonts.googleapis.com/css2?family=Archivo:wght@400;600;700&display=swap">
<style>
  :root {
    --frame: #bcbcb0;
    --paper: #ffffff;
    --navy: #003f66;
    --lime: #bed03f;
    --ink: #2b2b2b;
    --url-grey: #5a5a5a;
    --pattern-soft: #e6ecd8;
    --pattern-deep: #d3dde3;
  }
  * { margin: 0; padding: 0; box-sizing: border-box; }
  html, body {
    width: 1200px; height: 900px; overflow: hidden;
    background: var(--paper);
    font-family: "Archivo", Arial, sans-serif;
    color: var(--ink);
  }
  .canvas { position: relative; width: 1200px; height: 900px; }

  .card {
    position: absolute; top: 265px;
    width: 525px; height: 315px;
    background: var(--frame);
  }
  .card--front { left: 43px; }
  .card--back { left: 642px; }
  .card__face {
    position: absolute; left: 19px; top: 18px;
    width: 488px; height: 279px;
    background: var(--paper);
    overflow: hidden;
  }

  /* Front */
  .contact { position: absolute; left: 48px; top: 56px; }
  .contact__name { font-size: 19px; line-height: 22px; font-weight: 700; letter-spacing: 0.3px; color: var(--ink); }
  .contact__role { margin-top: 12px; font-size: 13px; line-height: 16px; font-weight: 400; }
  .contact__lines { margin-top: 20px; font-size: 13px; line-height: 18.5px; }
  .contact__line { display: flex; }
  .contact__label { width: 44px; font-weight: 400; }
  .contact__plus { font-weight: 400; margin-right: 4px; }
  .contact__value { font-weight: 700; font-size: 13.5px; letter-spacing: 0.4px; }
  .contact__email { margin-top: 23px; font-size: 12.5px; line-height: 16px; font-weight: 700; }
  .contact__address { margin-top: 6px; font-size: 10.5px; line-height: 14px; font-weight: 400; color: var(--url-grey); }

  .brand-mark {
    position: absolute; left: 334px; top: 119px;
    display: flex; align-items: center; gap: 7px;
  }
  .brand-mark__dot { width: 14px; height: 14px; border-radius: 50%; background: var(--lime); }
  .brand-mark__name { font-size: 20px; font-weight: 700; color: var(--navy); }

  /* Back */
  .pattern-field {
    position: absolute; inset: 0;
    background: linear-gradient(135deg, var(--pattern-soft) 0%, var(--pattern-deep) 50%, var(--pattern-soft) 100%);
  }
  .wordmark {
    position: absolute; left: 48px; right: 48px; top: 92px; height: 112px;
    padding-top: 10px;
    background: var(--paper);
    text-align: center;
  }
  .wordmark__name {
    font-size: 46px; font-weight: 700; color: var(--navy);
    letter-spacing: -0.5px; line-height: 1;
  }
  .wordmark__url {
    margin-top: 6px; font-size: 13.5px; line-height: 16px; font-weight: 700;
    color: var(--url-grey); letter-spacing: 0.4px;
  }
  .wordmark__tagline {
    margin-top: 6px; font-size: 9.5px; line-height: 13px; font-weight: 600;
    color: var(--navy);
  }
  .mascot {
    position: absolute; right: 14px; bottom: 10px;
    width: 62px; height: 62px; border-radius: 10px;
    background: linear-gradient(160deg, var(--lime), var(--navy));
  }
</style>
</head>
<body>
<main class="canvas">

  <section class="card card--front" aria-label="Business card front">
    <div class="card__face">
      <div class="contact">
        <h1 class="contact__name">Maria Hollingby</h1>
        <p class="contact__role">Business Development Manager</p>
        <div class="contact__lines">
          <p class="contact__line"><span class="contact__label">Tell</span><span class="contact__plus">+</span><span class="contact__value">61 7 3590 2481</span></p>
          <p class="contact__line"><span class="contact__label">Fax</span><span class="contact__plus">+</span><span class="contact__value">61 7 3648 2057</span></p>
          <p class="contact__line"><span class="contact__label">Mobil</span><span class="contact__plus">+</span><span class="contact__value">61 4 2751 6093</span></p>
        </div>
        <p class="contact__email">maria.hollingby@velocrine.com.au</p>
        <p class="contact__address">1947 Kelmott Street Parvale Queesnland 4213 Australia</p>
      </div>
      <div class="brand-mark">
        <span class="brand-mark__dot"></span>
        <span class="brand-mark__name">Velocrine</span>
      </div>
    </div>
  </section>

  <section class="card card--back" aria-label="Business card back">
    <div class="card__face">
      <div class="pattern-field" role="img" aria-label="Decorative brand pattern of navy and lime dots across the card"></div>
      <div class="wordmark">
        <p class="wordmark__name">Velocrine</p>
        <p class="wordmark__url">velocrine.com.au</p>
        <p class="wordmark__tagline">A Global Biopharmaceutical Contract Development Manufacturing Company</p>
      </div>
      <div class="mascot" role="img" aria-label="Cartoon mascot Tobin Wuzzle"></div>
    </div>
  </section>

</main>
</body>
</html>
```